Maple Ridge business card design

Card needs to include the following text/items:
Company Logo
Rupert Hollis
Phone # - 517-386-9042
service@mapleridgelandscaping.example
Lawn & landscape maintenance services

```html
<!DOCTYPE html>
<html lang="en">
<head>
<meta charset="utf-8">
<title>Maple Ridge Landscaping – Business Card</title>
<link href="https://fonts.googleapis.com/css2?family=Cinzel:wght@500;600&family=Arimo:wght@400&display=swap" rel="stylesheet">
<style>
  :root {
    --page-bg: #e8e5e0;
    --card-white: #f7f7f6;
    --forest: #1f5a33;
    --forest-deep: #17482a;
    --leaf: #5e8d2a;
    --leaf-light: #8fbf4c;
    --sky: #4aa6d8;
    --text-green: #1e5630;
    --white: #ffffff;
  }
  * { box-sizing: border-box; margin: 0; padding: 0; }
  html, body {
    width: 1200px; height: 960px; overflow: hidden;
    background: var(--page-bg);
  }
  .canvas {
    position: relative; width: 1200px; height: 960px;
  }
  .card {
    position: absolute; left: 250px; width: 700px; height: 400px;
    box-shadow: 0 6px 18px rgba(0,0,0,0.18);
    overflow: hidden;
  }
  .card--back { top: 50px; background: var(--forest); }
  .card--front { top: 510px; background: var(--card-white); }

  .card-art { position: absolute; inset: 0; width: 700px; height: 400px; display: block; }

  .brand-name {
    font-family: "Cinzel", serif; font-weight: 600; fill: var(--white);
  }

  .divider {
    position: absolute; left: 120px; top: 236px; width: 520px; height: 1px;
    background: var(--leaf);
  }

  .logo {
    position: absolute; right: 60px; top: 58px;
    display: flex; align-items: center; gap: 14px;
  }
  .logo-mark {
    width: 72px; height: 72px; border-radius: 50%;
    border: 3px solid var(--leaf);
  }
  .logo-name {
    font-family: "Cinzel", serif; font-weight: 600; color: var(--forest);
    font-size: 30px; line-height: 1.05;
  }
  .logo-name span { display: block; font-size: 15px; letter-spacing: 6px; }

  .holder-name {
    position: absolute; right: 60px; top: 262px;
    font-family: "Cinzel", serif; font-weight: 500; color: var(--leaf);
    font-size: 30px; letter-spacing: 1px;
  }

  .contact {
    position: absolute; left: 40px; top: 256px;
    font-family: "Arimo", sans-serif; color: var(--text-green);
    font-size: 16px; list-style: none;
  }
  .contact li { display: flex; align-items: center; gap: 9px; height: 26px; }
  .contact svg { width: 15px; height: 15px; fill: var(--leaf); flex: none; }
  .tagline {
    position: absolute; left: 30px; top: 360px;
    font-family: "Arimo", sans-serif; color: var(--text-green); font-size: 16px;
  }
</style>
</head>
<body>
<main class="canvas">

  <section class="card card--back" aria-label="Card back">
    <svg class="card-art" viewBox="0 0 700 400" xmlns="http://www.w3.org/2000/svg">
      <defs>
        <linearGradient id="band" x1="0" y1="0" x2="1" y2="1">
          <stop offset="0" stop-color="#1d5733"/>
          <stop offset="1" stop-color="#2a6a44"/>
        </linearGradient>
      </defs>
      <rect class="band" width="700" height="400" fill="url(#band)"/>
      <path class="scene" role="img" aria-label="Illustration of a sunny sky over rolling green hills"
            d="M250 0 Q160 200 240 400 L700 400 L700 0 Z" fill="#4aa6d8"/>
      <path class="band-edge" d="M236 0 Q146 200 226 400" fill="none" stroke="#8fbf4c" stroke-width="3"/>
      <text class="brand-name" x="470" y="112" text-anchor="middle" font-size="54">MAPLE RIDGE</text>
      <text class="brand-name" x="470" y="150" text-anchor="middle" font-size="20" letter-spacing="14">LANDSCAPING</text>
    </svg>
  </section>

  <section class="card card--front" aria-label="Card front">
    <div class="logo">
      <div class="logo-mark"></div>
      <div class="logo-name">Maple Ridge<span>LANDSCAPING</span></div>
    </div>

    <div class="divider"></div>

    <ul class="contact">
      <li>
        <svg viewBox="0 0 24 24" aria-hidden="true"><path d="M6.6 10.8a15 15 0 0 0 6.6 6.6l2.2-2.2c.3-.3.7-.4 1-.2 1.1.4 2.3.6 3.6.6.6 0 1 .4 1 1V20c0 .6-.4 1-1 1A17 17 0 0 1 3 4c0-.6.4-1 1-1h3.5c.6 0 1 .4 1 1 0 1.3.2 2.5.6 3.6.1.3 0 .7-.2 1z"/></svg>
        517-386-9042
      </li>
      <li>
        <svg viewBox="0 0 24 24" aria-hidden="true"><path d="M2 5h20v14H2z M3.5 6.5 12 13l8.5-6.5" fill="none" stroke="#5e8d2a" stroke-width="2"/></svg>
        service@mapleridgelandscaping.example
      </li>
      <li>
        <svg viewBox="0 0 24 24" aria-hidden="true"><circle cx="12" cy="12" r="10" fill="none" stroke="#5e8d2a" stroke-width="2"/><path d="M2 12h20M12 2c3 3 3 17 0 20M12 2c-3 3-3 17 0 20" fill="none" stroke="#5e8d2a" stroke-width="1.6"/></svg>
        www.mapleridgelandscaping.example
      </li>
    </ul>
    <p class="tagline">Lawn &amp; landscape maintenance services</p>

    <p class="holder-name">Rupert Hollis</p>
  </section>

</main>
</body>
</html>
```